Redesign the Eshop of a gift shop

We want to redesign the front page, the category page and the product page of our Eshop that sells gifts.
I am thinking not to reveal the url of the eshop as i don't want you to get influenced. Lets call the Eshop "PresentNest.com"
I will list the brands that we resell so you understand what we are selling,
Morvato-https://www.morvato-example.com/
Zandorpel-https://zandorpel-example.com/
Vamtol - https://vamtol-example.com/
Quiet Orchard - https://www.quietorchard-example.com/
Ranger's Workbench - https://rangersworkbench-example.com/
Plumeline press - https://plumelinepress-example.com/
Tarpawn - https://tarpawnofficial-example.com/
We also sell toys for adults like backgamon, chess, playing cards, board games.
The problem is that many eshops sell these and thats why i would like the design to have a different approach, more fresh, not seen before.
I am also thinking of something playfull, happy, but warm at the same time.
Please note that our logo is black & white but feel free to play with any color/s you like in your website design. We might eventually even adjust the logo colors, or you can provide a pallete that suites a black and white logo
Let me know if you have any questions!
Updates
A couple of designers kindly asked to extend so they can submit.
Target Market(s)
Age: 20-50, Gender: Also men but mostly women, Income: Moderate to high, Interests and Lifestyle: Customers who value sentimentality, personal connection, and thoughtful gestures, Relationship Status: Those in relationships or with larger families
Number of Pages Required
3 page
Look and feel
Each slider illustrates characteristics of the customer's brand and the style your logo design should communicate.

```html
<!DOCTYPE html>
<html lang="en">
<head>
<meta charset="utf-8">
<title>PresentNest – Gifts with a personal touch</title>
<link href="https://fonts.googleapis.com/css2?family=Roboto+Condensed:wght@300;400;700&family=Poppins:wght@300;400;500;600;700&display=swap" rel="stylesheet">
<style>
:root{
  --orange:#f8a724;
  --orange-dark:#ef8f12;
  --black:#121212;
  --ink:#1d1d1d;
  --grey:#6f6f6f;
  --soft:#efefef;
  --line:#e4e4e4;
  --white:#ffffff;
}
*{margin:0;padding:0;box-sizing:border-box}
html,body{width:1200px;height:5150px;overflow:hidden;background:var(--white)}
body{font-family:"Poppins",sans-serif;color:var(--ink);position:relative}
.page{position:relative;width:1200px;height:5150px;overflow:hidden}
.abs{position:absolute}
.ph{position:absolute;display:block}
a{color:inherit;text-decoration:none}

/* top bar */
.topbar{top:0;left:0;width:1200px;height:36px;background:var(--orange);font-size:11px;color:var(--black)}
.topbar .item{position:absolute;top:11px;display:flex;align-items:center;gap:5px}
.topbar .social{position:absolute;top:11px;left:252px;display:flex;gap:12px}
.topbar .social span{width:12px;height:12px;border-radius:50%;background:var(--black)}
.topbar .sep{position:absolute;top:10px;width:1px;height:16px;background:rgba(0,0,0,.35)}

/* header */
.header{top:36px;left:0;width:1200px;height:92px;background:var(--white)}
.logo{position:absolute;display:flex;align-items:center;gap:8px;font-family:"Poppins",sans-serif;font-weight:500;letter-spacing:3px;color:var(--black)}
.logo .mark{width:14px;height:14px;background:var(--black)}
.header .logo{left:162px;top:40px;font-size:26px}
.search{position:absolute;left:380px;top:30px;width:322px;height:42px;border-radius:21px;background:var(--white);box-shadow:0 2px 8px rgba(0,0,0,.12)}
.search .cat{position:absolute;left:0;top:0;width:100px;height:42px;border-radius:21px;background:var(--orange);font-size:12px;font-weight:600;display:flex;align-items:center;justify-content:center}
.search .ph-text{position:absolute;left:124px;top:13px;font-size:11px;color:#8a8a8a}
.search .go{position:absolute;right:6px;top:6px;width:30px;height:30px;border-radius:50%;background:var(--orange);display:flex;align-items:center;justify-content:center}
.hicon{position:absolute;top:22px;text-align:center;font-size:11px;color:var(--black)}
.hicon svg{display:block;margin:0 auto 6px}
.hsep{position:absolute;top:38px;width:1px;height:28px;background:var(--line)}

/* nav */
.nav{top:128px;left:0;width:1200px;height:54px;background:var(--black)}
.nav a{position:absolute;top:21px;font-size:11px;color:var(--white);letter-spacing:.3px}

/* hero */
.hero{top:182px;left:0;width:1200px;height:530px;background:var(--black);overflow:hidden}
.hero h1{position:absolute;left:166px;top:124px;font-family:"Roboto Condensed",sans-serif;color:var(--white);line-height:1}
.hero h1 .l1{display:block;font-weight:300;font-size:70px}
.hero h1 .l2{display:block;font-weight:700;font-size:86px;margin-top:2px}
.hero p{position:absolute;left:168px;top:290px;width:470px;font-size:14px;line-height:26px;color:var(--white)}
.btn{display:inline-flex;align-items:center;justify-content:center;background:var(--orange);color:var(--black);font-weight:700;border-radius:20px;font-size:10px;letter-spacing:.3px}
.hero .btn{position:absolute;left:162px;top:356px;width:102px;height:28px}

/* section headings */
.h2{position:absolute;font-family:"Roboto Condensed",sans-serif;font-weight:700;font-size:28px;color:var(--black);letter-spacing:.2px}
.h2::after{content:"";position:absolute;left:0;top:50px;width:56px;height:4px;background:var(--orange);border-radius:2px}
.h2.center::after{left:50%;margin-left:-28px}
.more{position:absolute;font-size:10px;font-weight:600;color:var(--black);display:flex;align-items:center;gap:8px}
.more::after{content:"";border-left:7px solid var(--orange);border-top:4px solid transparent;border-bottom:4px solid transparent}
.arrow{position:absolute;width:20px;height:24px}

/* categories */
.catcard{position:absolute;background:var(--white);border:1px solid var(--line);border-radius:3px;text-align:center;font-family:"Roboto Condensed",sans-serif;font-weight:700;font-size:14px}
.catcard.active{box-shadow:0 4px 16px rgba(0,0,0,.14);font-size:18px}
.catcard .label{position:absolute;left:0;right:0}

/* products */
.prod{position:absolute;width:430px;height:280px;background:var(--white);box-shadow:0 1px 8px rgba(0,0,0,.09)}
.prod .img{position:absolute;left:22px;top:0;width:158px;height:280px;background:var(--soft)}
.prod .txt{position:absolute;left:222px;top:60px}
.prod h3{font-family:"Roboto Condensed",sans-serif;font-weight:700;font-size:17px;color:var(--black)}
.prod .sub{font-size:13px;margin-top:8px;letter-spacing:.3px}
.prod .save{font-size:10px;margin-top:12px}
.prod .old{position:absolute;left:110px;top:76px;font-size:11px;text-decoration:line-through}
.prod .now{font-size:12px;margin-top:12px;font-weight:500}
.prod .btn{margin-top:18px;width:102px;height:26px}
.wide-btn{position:absolute;left:490px;top:1990px;width:218px;height:38px;font-size:11px}

/* featured */
.feat{position:absolute;border-radius:4px;overflow:hidden}
.feat .cap{position:absolute;left:28px;bottom:24px;color:var(--white)}
.feat .cap b{display:block;font-family:"Roboto Condensed",sans-serif;font-size:15px;margin-bottom:6px}
.feat .pill{display:inline-block;background:var(--orange);color:var(--black);border-radius:10px;font-size:11px;font-weight:600;padding:2px 12px;margin-right:18px}
.feat .pl{font-size:9px}

/* reviews */
.review{position:absolute;top:2614px;height:160px;background:var(--white);border:1px solid var(--line);box-shadow:0 1px 6px rgba(0,0,0,.06)}
.review .av{position:absolute;left:28px;top:22px;width:56px;height:56px;border-radius:50%}
.review .who{position:absolute;left:8px;top:86px;width:100px;text-align:center;font-size:10px;font-weight:600}
.review .who small{display:block;font-weight:400;font-size:8px;margin-top:4px}
.review .who .stars{color:var(--orange);font-size:9px;letter-spacing:1px}
.review .body{position:absolute;left:112px;top:32px;width:158px;text-align:center}
.review .body b{display:block;font-family:"Roboto Condensed",sans-serif;font-size:12px}
.review .body p{font-size:8px;line-height:15px;margin-top:4px;color:#333}

/* blog */
.post-main{position:absolute;left:572px;top:2958px;width:464px;height:290px;background:#f7f7f7}
.post-main h3{position:absolute;left:48px;top:40px;width:360px;font-family:"Roboto Condensed",sans-serif;font-size:22px;line-height:28px;font-weight:700}
.meta{display:flex;align-items:center;gap:8px}
.post-main .date{position:absolute;left:48px;top:120px;font-size:12px}
.post-main p{position:absolute;left:46px;top:164px;width:390px;font-size:12px;line-height:24px}
.author{position:absolute;display:flex;align-items:center;gap:10px;font-weight:500}
.author .dot{border-radius:50%;background:#8797a8}
.stats{position:absolute;display:flex;gap:14px}
.post-sm .t{position:absolute;font-family:"Roboto Condensed",sans-serif;font-size:12px;font-weight:700;line-height:15px}
.post-sm .d{position:absolute;font-size:8px}
.post-sm p{position:absolute;font-size:9px;line-height:15px;width:214px}

/* brands */
.brand{position:absolute;top:3688px;font-family:"Poppins",sans-serif;font-weight:600;font-size:19px;color:var(--black);display:flex;align-items:center;gap:8px;white-space:nowrap}
.brand .sq{width:12px;height:12px;background:var(--orange)}

/* newsletter */
.news h3{position:absolute;left:614px;top:4296px;font-family:"Roboto Condensed",sans-serif;font-weight:700;font-size:28px}
.news .field{position:absolute;left:606px;top:4352px;width:432px;height:46px;border-radius:23px;background:var(--white);box-shadow:0 2px 10px rgba(0,0,0,.13)}
.news .field span{position:absolute;left:40px;top:15px;font-size:12px;color:#444}
.news .field .btn{position:absolute;right:4px;top:4px;width:116px;height:38px;font-size:11px;border-radius:19px}
.news .box{position:absolute;left:650px;top:4436px;width:14px;height:14px;border:1px solid #555}
.news p{position:absolute;left:680px;top:4432px;width:350px;font-size:11px;line-height:21px}

/* features band */
.band{top:4572px;left:0;width:1200px;height:184px;background:var(--orange)}
.feature{position:absolute;top:76px;display:flex;align-items:center;gap:10px}
.feature small{display:block;font-size:10px;font-weight:600;color:var(--white)}
.feature b{display:block;font-size:14px;font-weight:600;color:var(--black)}

/* footer */
.footer{top:4756px;left:0;width:1200px;height:394px;background:var(--black);color:var(--white)}
.footer h4{position:absolute;top:80px;font-size:15px;font-weight:600}
.footer ul{position:absolute;list-style:none;font-size:11px}
.footer li{height:35px;display:flex;align-items:flex-start;gap:10px}
.footer li::before{content:"›";font-size:13px;line-height:14px;color:var(--white)}
.contact{position:absolute;left:536px;display:flex;gap:14px;font-size:12px;line-height:22px}
.contact .ic{width:28px;height:28px;border-radius:50%;background:var(--orange);flex:none;display:flex;align-items:center;justify-content:center}
.contact b{font-weight:500;font-size:13px}
.footer .logo{left:836px;top:166px;font-size:32px;color:var(--white)}
.footer .logo .mark{background:var(--white)}
.fsoc{position:absolute;left:864px;top:238px;display:flex;gap:8px}
.fsoc span{width:30px;height:30px;border-radius:50%;border:1.5px solid var(--white)}
.copy{position:absolute;left:0;top:354px;width:1200px;text-align:center;font-size:10px;border-top:1px solid #2a2a2a;padding-top:12px}
</style>
</head>
<body>
<div class="page">

  <!-- top bar -->
  <div class="abs topbar">
    <div class="item" style="left:162px"><svg width="13" height="12" viewBox="0 0 24 22"><path d="M12 21 2.5 11.5A5.5 5.5 0 0 1 12 4a5.5 5.5 0 0 1 9.5 7.5Z" fill="none" stroke="#121212" stroke-width="2.4"/></svg>Wishlist</div>
    <div class="sep" style="left:244px"></div>
    <div class="social"><span></span><span></span><span></span><span></span></div>
    <div class="item" style="left:496px"><svg width="12" height="12" viewBox="0 0 12 12"><rect x="1" y="3" width="10" height="8" fill="#121212"/><path d="M4 3V1h4v2" fill="none" stroke="#121212"/></svg>My Orders</div>
    <div class="item" style="left:594px"><svg width="11" height="11" viewBox="0 0 12 12"><path d="M5 2 1 6l4 4M1 6h10" fill="none" stroke="#121212" stroke-width="2"/></svg>Complaints &amp; Returns</div>
    <div class="item" style="left:746px">? Help &amp; Contact</div>
    <div class="item" style="left:862px"><svg width="12" height="12" viewBox="0 0 12 12"><path d="M1 6 6 1l5 5v5H1Z" fill="#121212"/></svg>Home Club</div>
    <div class="item" style="left:964px"><svg width="13" height="11" viewBox="0 0 13 11"><rect width="13" height="11" rx="2" fill="#121212"/></svg>Rewards</div>
  </div>

  <!-- header -->
  <div class="abs header">
    <div class="logo"><span class="mark"></span>PRESENTNEST</div>
    <div class="search">
      <div class="cat">Categories</div>
      <div class="ph-text">Search Here....</div>
      <div class="go"><svg width="14" height="14" viewBox="0 0 14 14"><circle cx="6" cy="6" r="4.5" fill="none" stroke="#121212" stroke-width="1.8"/><path d="m9.5 9.5 3.5 3.5" stroke="#121212" stroke-width="1.8"/></svg></div>
    </div>
    <div class="hicon" style="left:740px"><svg width="18" height="20" viewBox="0 0 18 20"><circle cx="9" cy="5" r="4.5" fill="#121212"/><path d="M0 20a9 8 0 0 1 18 0Z" fill="#121212"/></svg>Log In ⌄</div>
    <div class="hsep" style="left:806px"></div>
    <div class="hicon" style="left:838px"><svg width="22" height="20" viewBox="0 0 22 20"><path d="M2 6h18l-2 13H4Z" fill="#121212"/><path d="M7 6a4 4 0 0 1 8 0" fill="none" stroke="#121212" stroke-width="1.8"/><circle cx="18" cy="3" r="3" fill="#e8411f"/></svg>Shopping cart ⌄</div>
    <div class="hsep" style="left:956px"></div>
    <div class="hicon" style="left:982px"><svg width="22" height="22" viewBox="0 0 22 22" fill="none" stroke="#121212" stroke-width="1.4"><circle cx="11" cy="11" r="9.5"/><ellipse cx="11" cy="11" rx="4.5" ry="9.5"/><path d="M1.5 11h19M3 6h16M3 16h16"/></svg>English ⌄</div>
  </div>

  <!-- navigation -->
  <nav class="abs nav">
    <a style="left:162px">HOME</a>
    <a style="left:260px">SHOP BY CATEGORY</a>
    <a style="left:428px">SHOP BY INTEREST</a>
    <a style="left:590px">ABOUT US</a>
    <a style="left:708px">E-GIFT CARD</a>
    <a style="left:842px">WHOLESALE</a>
    <a style="left:972px">CONTACT US</a>
  </nav>

  <!-- hero -->
  <section class="abs hero">
    <svg class="ph" style="left:0;top:0" width="1200" height="530" viewBox="0 0 1200 530">
      <polygon points="0,0 112,0 0,78" fill="#f8a724"/>
      <polygon points="0,470 0,530 12,530 12,470" fill="#f8a724"/>
      <polygon points="130,0 420,0 260,120" fill="#1c1c1c"/>
      <polygon points="360,210 620,60 700,260" fill="#1a1a1a"/>
      <polygon points="820,530 1200,170 1200,530" fill="#f8a724"/>
      <circle cx="800" cy="450" r="200" fill="#ffffff"/>
      <polygon points="632,184 682,224 662,132" fill="#f8a724" stroke="#ffffff" stroke-width="3"/>
      <polygon points="690,120 752,104 706,190" fill="#ef6a1c"/>
      <polygon points="1080,200 1150,160 1140,230" fill="#ffffff"/>
    </svg>
    <div class="ph" role="img" aria-label="Smiling woman in a polka dot blouse holding a pink leather handbag" style="left:650px;top:0;width:330px;height:530px;border-radius:160px 160px 0 0;background:linear-gradient(180deg,#c99a7f 0%,#ece6df 45%,#b89892 100%)"></div>
    <h1><span class="l1">NEW</span><span class="l2">COLLECTION</span></h1>
    <p>Lorem ipsum dolor sit amet, consectetuer adipiscing elit, sed diam nonummy nibh euismod tincidunt</p>
    <a class="btn">SHOP NOW</a>
  </section>

  <!-- shop by categories -->
  <h2 class="h2" style="left:160px;top:804px">SHOP BY CATEGORIES</h2>
  <a class="more" style="left:880px;top:820px">SHOW ALL CATEGORIES</a>
  <svg class="arrow" style="left:126px;top:1014px" viewBox="0 0 20 24"><path d="M14 2 4 12l10 10" fill="none" stroke="#999" stroke-width="2"/></svg>
  <svg class="arrow" style="left:1054px;top:1014px" viewBox="0 0 20 24"><path d="M6 2l10 10L6 22" fill="none" stroke="#999" stroke-width="2"/></svg>

  <div class="catcard" style="left:162px;top:898px;width:188px;height:268px">
    <div class="ph" role="img" aria-label="Black lace dress and patterned top on hangers" style="left:40px;top:14px;width:108px;height:176px;background:linear-gradient(180deg,#d8c7ab,#1e1e1e)"></div>
    <div class="label" style="top:216px">CLOTHING</div>
  </div>
  <div class="catcard active" style="left:380px;top:876px;width:222px;height:312px">
    <div class="ph" role="img" aria-label="Orange leather handbag" style="left:26px;top:34px;width:170px;height:170px;background:linear-gradient(160deg,#f26a3c,#c2391b);border-radius:6px"></div>
    <div class="label" style="top:236px">BAGS</div>
  </div>
  <div class="catcard" style="left:632px;top:898px;width:188px;height:268px">
    <div class="ph" role="img" aria-label="White mug with a red heart message" style="left:34px;top:40px;width:120px;height:130px;background:linear-gradient(135deg,#f4f4f4,#d9d9d9);border-radius:6px"></div>
    <div class="label" style="top:216px">MUGS</div>
  </div>
  <div class="catcard" style="left:850px;top:898px;width:188px;height:268px">
    <div class="ph" role="img" aria-label="Brown leather wallet" style="left:34px;top:52px;width:122px;height:110px;background:linear-gradient(150deg,#c06a2b,#7d3a14);border-radius:6px"></div>
    <div class="label" style="top:216px">WALLETS</div>
  </div>

  <!-- bestsellers -->
  <h2 class="h2" style="left:160px;top:1278px">OUR BESTSELLER PRODUCTS</h2>

  <div class="prod" style="left:160px;top:1352px">
    <div class="img" role="img" aria-label="Tartan card holder"><div style="position:absolute;left:44px;top:58px;width:76px;height:164px;background:linear-gradient(135deg,#a3623d,#6e3a22)"></div></div>
    <div class="txt"><h3>LOREM IPSUM SIT DO</h3><div class="sub">SIT DOLOR AMED</div><div class="save">Save Upto 38%</div><div class="old">$ 248.00</div><div class="now">ONLY $ 148.00</div><a class="btn">SHOP NOW</a></div>
  </div>
  <div class="prod" style="left:608px;top:1352px">
    <div class="img" role="img" aria-label="Enamel mug printed with mushrooms"><div style="position:absolute;left:30px;top:90px;width:100px;height:100px;background:linear-gradient(135deg,#f3efe8,#d9cfc2);border-radius:10px"></div></div>
    <div class="txt"><h3>LOREM IPSUM SIT DO</h3><div class="sub">SIT DOLOR AMED</div><div class="save">Save Upto 38%</div><div class="old">$ 248.00</div><div class="now">ONLY $ 148.00</div><a class="btn">SHOP NOW</a></div>
  </div>
  <div class="prod" style="left:160px;top:1674px">
    <div class="img" role="img" aria-label="Colourful spiral notebook"><div style="position:absolute;left:30px;top:64px;width:100px;height:140px;background:linear-gradient(135deg,#f0a3c1,#f4c36a 60%,#8ab9e6)"></div></div>
    <div class="txt"><h3>LOREM IPSUM SIT DO</h3><div class="sub">SIT DOLOR AMED</div><div class="save">Save Upto 38%</div><div class="old">$ 248.00</div><div class="now">ONLY $ 148.00</div><a class="btn">SHOP NOW</a></div>
  </div>
  <div class="prod" style="left:608px;top:1674px">
    <div class="img" role="img" aria-label="Fire starter tool in its packaging"><div style="position:absolute;left:36px;top:30px;width:86px;height:220px;background:linear-gradient(180deg,#3a4350,#1e242c);border-radius:6px"></div></div>
    <div class="txt"><h3>LOREM IPSUM SIT DO</h3><div class="sub">SIT DOLOR AMED</div><div class="save">Save Upto 38%</div><div class="old">$ 248.00</div><div class="now">ONLY $ 148.00</div><a class="btn">SHOP NOW</a></div>
  </div>
  <a class="btn wide-btn">VIEW ALL CURRENT OFFERS</a>

  <div class="abs" style="left:160px;top:2078px;width:880px;height:1px;background:var(--line)"></div>

  <!-- featured -->
  <h2 class="h2" style="left:160px;top:2124px">FEATURED PRODUCTS</h2>
  <a class="more" style="left:880px;top:2134px">SHOW ALL CATEGORIES</a>
  <svg class="arrow" style="left:126px;top:2316px" viewBox="0 0 20 24"><path d="M14 2 4 12l10 10" fill="none" stroke="#999" stroke-width="2"/></svg>
  <svg class="arrow" style="left:1054px;top:2316px" viewBox="0 0 20 24"><path d="M6 2l10 10L6 22" fill="none" stroke="#999" stroke-width="2"/></svg>

  <div class="feat" style="left:162px;top:2198px;width:316px;height:248px;box-shadow:0 4px 14px rgba(0,0,0,.25)">
    <div class="ph" role="img" aria-label="Wooden backgammon board with checkers" style="inset:0;background:linear-gradient(150deg,#7a4b2e,#3b2217 55%,#1a120e)"></div>
    <div class="cap"><b>BACKGAMON</b><span class="pill">4556</span><span class="pl">PRODUCTS ▸</span></div>
  </div>
  <div class="feat" style="left:506px;top:2224px;width:254px;height:200px">
    <div class="ph" role="img" aria-label="Hand moving a chess piece" style="inset:0;background:linear-gradient(150deg,#a8754a,#4b2e1c 60%,#1f1510)"></div>
    <div class="cap"><b>CHESS</b><span class="pill">4556</span><span class="pl">PRODUCTS ▸</span></div>
  </div>
  <div class="feat" style="left:782px;top:2224px;width:256px;height:200px">
    <div class="ph" role="img" aria-label="Friends playing cards at a table" style="inset:0;background:linear-gradient(150deg,#d88a4a,#8a4522 60%,#3a1e12)"></div>
    <div class="cap"><b>PLAYING CARDS</b><span class="pill">4556</span><span class="pl">PRODUCTS ▸</span></div>
  </div>

  <div class="abs" style="left:160px;top:2494px;width:880px;height:1px;background:var(--line)"></div>

  <!-- reviews -->
  <h2 class="h2" style="left:160px;top:2542px">CUSTOMER REVIEWS</h2>
  <svg class="arrow" style="left:126px;top:2678px" viewBox="0 0 20 24"><path d="M14 2 4 12l10 10" fill="none" stroke="#999" stroke-width="2"/></svg>
  <svg class="arrow" style="left:1054px;top:2678px" viewBox="0 0 20 24"><path d="M6 2l10 10L6 22" fill="none" stroke="#999" stroke-width="2"/></svg>

  <div class="review" style="left:162px;width:276px">
    <div class="av" role="img" aria-label="Customer portrait" style="background:#e3cbb0"></div>
    <div class="who">Mara Lindqvist<small>March 24,2023</small><span class="stars">★★★★★</span></div>
    <div class="body"><b>LOREM IPSUM DOLOR</b><p>Lorem ipsum dolor sit amet, consectetur adipiscing elit, sed do eiusmod tempor incididunt ut labore et dolore magna aliqua Lorem ipsum dolor sit amet</p></div>
  </div>
  <div class="review" style="left:462px;width:278px">
    <div class="av" role="img" aria-label="Customer portrait" style="background:#b7a89d"></div>
    <div class="who">Tobin Areli<small>March 24,2023</small><span class="stars">★★★★★</span></div>
    <div class="body"><b>LOREM IPSUM DOLOR</b><p>Lorem ipsum dolor sit amet, consectetur adipiscing elit, sed do eiusmod tempor incididunt ut labore et dolore magna aliqua Lorem ipsum dolor sit amet</p></div>
  </div>
  <div class="review" style="left:762px;width:278px">
    <div class="av" role="img" aria-label="Customer portrait" style="background:#8e7b70"></div>
    <div class="who">Edie Varnell<small>March 24,2023</small><span class="stars">★★★★★</span></div>
    <div class="body"><b>LOREM IPSUM DOLOR</b><p>Lorem ipsum dolor sit amet, consectetur adipiscing elit, sed do eiusmod tempor incididunt ut labore et dolore magna aliqua Lorem ipsum dolor sit amet</p></div>
  </div>

  <!-- blog -->
  <h2 class="h2" style="left:160px;top:2868px">LATEST BLOG POSTS</h2>
  <a class="more" style="left:880px;top:2876px">SHOW ALL CATEGORIES</a>

  <div class="ph" role="img" aria-label="Stack of floral patterned notebooks and journals" style="left:162px;top:2940px;width:410px;height:324px;background:linear-gradient(135deg,#f1b98a,#e77f8c 40%,#6aa5c8 75%,#f4d46c)"></div>
  <div class="post-main">
    <h3>Lorem Ipsum Dolor Sit Amet Consectetur</h3>
    <div class="date meta"><svg width="13" height="13" viewBox="0 0 13 13"><rect x="1" y="2" width="11" height="10" fill="none" stroke="#121212"/><path d="M1 5h11" stroke="#121212"/></svg>&nbsp;Jul 22, 2023</div>
    <p>Lorem ipsum dolor sit amet, consectetur adipiscing elit, sed do eiusmod tempor incididunt ut labore et dolore magna</p>
    <div class="author" style="left:44px;top:246px;font-size:12px"><span class="dot" style="width:32px;height:32px"></span>BY NOA HALVERS</div>
    <div class="stats" style="left:282px;top:254px;font-size:11px"><span>◯ 5</span><span>♡ 2</span><span>◉ 14</span></div>
  </div>

  <svg class="arrow" style="left:126px;top:3374px" viewBox="0 0 20 24"><path d="M14 2 4 12l10 10" fill="none" stroke="#999" stroke-width="2"/></svg>
  <svg class="arrow" style="left:1054px;top:3374px" viewBox="0 0 20 24"><path d="M6 2l10 10L6 22" fill="none" stroke="#999" stroke-width="2"/></svg>

  <div class="post-sm">
    <div class="ph" role="img" aria-label="Two friends walking outdoors in summer clothes" style="left:162px;top:3310px;width:194px;height:142px;background:linear-gradient(160deg,#e8d8c4,#b38a6a 60%,#6d5b4e)"></div>
    <div class="ph" style="left:356px;top:3310px;width:232px;height:142px;background:#f7f7f7"></div>
    <div class="t" style="left:380px;top:3324px">Lorem Ipsum Dolor Sit Amet<br>Consectetur</div>
    <div class="d" style="left:380px;top:3364px">▭ Jul 22, 2023</div>
    <p style="left:380px;top:3382px">Lorem ipsum dolor sit amet, consectetur adipiscing elit sed do</p>
    <div class="author" style="left:378px;top:3422px;font-size:6px"><span class="dot" style="width:16px;height:16px"></span>BY NOA HALVERS</div>
    <div class="stats" style="left:492px;top:3426px;font-size:7px"><span>◯ 5</span><span>♡ 2</span><span>◉ 14</span></div>
  </div>
  <div class="post-sm">
    <div class="ph" role="img" aria-label="Chess pieces on a wooden board" style="left:620px;top:3310px;width:194px;height:142px;background:linear-gradient(160deg,#f1ece4,#b48b5f 55%,#2a231e)"></div>
    <div class="ph" style="left:814px;top:3310px;width:226px;height:142px;background:#f7f7f7"></div>
    <div class="t" style="left:836px;top:3324px">Lorem Ipsum Dolor Sit Amet<br>Consectetur</div>
    <div class="d" style="left:836px;top:3364px">▭ Jul 22, 2023</div>
    <p style="left:836px;top:3382px">Lorem ipsum dolor sit amet, consectetur adipiscing elit sed do</p>
    <div class="author" style="left:834px;top:3422px;font-size:6px"><span class="dot" style="width:16px;height:16px"></span>BY NOA HALVERS</div>
    <div class="stats" style="left:946px;top:3426px;font-size:7px"><span>◯ 5</span><span>♡ 2</span><span>◉ 14</span></div>
  </div>

  <svg class="abs" style="left:588px;top:3498px" width="36" height="12" viewBox="0 0 36 12"><circle cx="5" cy="6" r="2.5" fill="#121212"/><circle cx="18" cy="6" r="5" fill="#121212"/><circle cx="31" cy="6" r="2.5" fill="#121212"/></svg>

  <div class="abs" style="left:160px;top:3550px;width:880px;height:1px;background:var(--line)"></div>

  <!-- brands -->
  <h2 class="h2 center" style="left:0;width:1186px;text-align:center;top:3604px">THE BRANDS THAT WE RESELL</h2>
  <svg class="arrow" style="left:126px;top:3692px" viewBox="0 0 20 24"><path d="M14 2 4 12l10 10" fill="none" stroke="#999" stroke-width="2"/></svg>
  <svg class="arrow" style="left:1054px;top:3692px" viewBox="0 0 20 24"><path d="M6 2l10 10L6 22" fill="none" stroke="#999" stroke-width="2"/></svg>
  <div class="brand" style="left:164px"><span class="sq"></span>Morvato</div>
  <div class="brand" style="left:290px">Quiet Orchard</div>
  <div class="brand" style="left:510px">Zandorpel</div>
  <div class="brand" style="left:696px;font-size:16px">Ranger's Workbench</div>
  <div class="brand" style="left:912px">Tarpawn</div>

  <!-- instagram -->
  <h2 class="h2" style="left:160px;top:3820px">INSTAGRAM GALLERY</h2>
  <div class="ph" role="img" aria-label="Smiling man with a backpack on a city street" style="left:0;top:3910px;width:284px;height:274px;background:linear-gradient(150deg,#cfc3b1,#7b6652 60%,#3d3128)"></div>
  <div class="ph" role="img" aria-label="Hands holding a red leather wallet" style="left:292px;top:3896px;width:324px;height:306px;background:linear-gradient(150deg,#d7d2cb,#b2432a 55%,#4d2a21)"></div>
  <div class="ph" role="img" aria-label="Hands writing in a notebook at a desk" style="left:624px;top:3910px;width:278px;height:274px;background:linear-gradient(150deg,#3c4250,#7d7568 55%,#262a31)"></div>
  <div class="ph" role="img" aria-label="Woman in sunglasses carrying a white handbag" style="left:914px;top:3910px;width:286px;height:270px;background:linear-gradient(150deg,#b6c7d3,#e9e3d8 50%,#9f8a70)"></div>

  <!-- newsletter -->
  <section class="news">
    <div class="ph" role="img" aria-label="Woman in a beige knit outfit sitting at a laptop" style="left:140px;top:4244px;width:420px;height:328px;background:linear-gradient(180deg,#ffffff 0%,#e9d6c6 35%,#b88c70 100%)"></div>
    <h3>SIGN UP FOR NEWSLETTER</h3>
    <div class="field"><span>Enter Email Id</span><a class="btn">Submit</a></div>
    <div class="box"></div>
    <p>Lorem ipsum dolor sit amet, consectetur adipiscing elit, sed do eiusmod tempor incididunt ut labore et dolore magna aliqua. Ut enim ad minim veniam, quis nostrud exercitation ullamco laboris Lorem ipsum dolor sit amet</p>
  </section>

  <!-- features band -->
  <section class="abs band">
    <div class="feature" style="left:162px">
      <svg width="38" height="38" viewBox="0 0 38 38" fill="none" stroke="#121212" stroke-width="2"><path d="M8 18h6v14H8ZM14 20l6-10c2 0 3 2 2 5h8c2 0 3 2 2 4l-3 10c-1 2-2 3-4 3H14"/></svg>
      <div><small>100% Guarantee</small><b>Moneyback Guarantee</b></div>
    </div>
    <div class="feature" style="left:432px">
      <svg width="38" height="38" viewBox="0 0 38 38" fill="none" stroke="#121212" stroke-width="2"><rect x="4" y="12" width="30" height="22"/><path d="M4 18h30M19 12v22M19 12c-4-8-10-6-8-2M19 12c4-8 10-6 8-2"/></svg>
      <div><small>Purchase</small><b>Free Shipping</b></div>
    </div>
    <div class="feature" style="left:648px">
      <svg width="38" height="38" viewBox="0 0 38 38" fill="none" stroke="#121212" stroke-width="2"><path d="M19 3 33 8v10c0 9-6 14-14 17C11 32 5 27 5 18V8Z"/><circle cx="19" cy="18" r="7"/><path d="M19 13v10M17 15h3M17 21h3"/></svg>
      <div><small>Money</small><b>Secure Payment</b></div>
    </div>
    <div class="feature" style="left:876px">
      <svg width="38" height="38" viewBox="0 0 38 38" fill="none" stroke="#121212" stroke-width="2"><circle cx="19" cy="20" r="14"/><circle cx="19" cy="20" r="8"/><path d="M5 14a14 14 0 0 1 28 0"/></svg>
      <div><small>24/7 Support</small><b>Online Support</b></div>
    </div>
  </section>

  <!-- footer -->
  <footer class="abs footer">
    <h4 style="left:164px">Quick Links</h4>
    <ul style="left:164px;top:120px">
      <li>Shop by Category</li><li>Shop by Interest</li><li>About Us</li><li>E-Gift Card</li><li>Wholesale</li><li>Contact Us</li>
    </ul>
    <ul style="left:332px;top:120px">
      <li>Payment &amp; Order</li><li>Shipping &amp; Delivery</li><li>Exchange &amp; Return</li><li>Authenticity Check</li><li>Warranty</li><li>FAQs</li>
    </ul>
    <h4 style="left:536px">Contact Details</h4>
    <div class="contact" style="top:118px">
      <span class="ic"><svg width="12" height="14" viewBox="0 0 12 14"><path d="M6 14S1 8 1 5a5 5 0 0 1 10 0c0 3-5 9-5 9Z" fill="#121212"/><circle cx="6" cy="5" r="2" fill="#f8a724"/></svg></span>
      <div><b>Address</b><br>12 Lorem Imsum, Street Name,<br>City Name, Country - 12345</div>
    </div>
    <div class="contact" style="top:204px">
      <span class="ic"><svg width="13" height="13" viewBox="0 0 13 13"><path d="M3 1 5 4 3.5 5.5a8 8 0 0 0 4 4L9 8l3 2-1.5 2.5C5 12 1 8 .5 2.5Z" fill="#121212"/></svg></span>
      <div><b>Phone</b><br>123.456.7890</div>
    </div>
    <div class="contact" style="top:272px">
      <span class="ic"><svg width="14" height="10" viewBox="0 0 14 10"><rect width="14" height="10" fill="#121212"/><path d="M0 0l7 5 7-5" fill="none" stroke="#f8a724"/></svg></span>
      <div><b>Email</b><br>inquiry@presentnest.com</div>
    </div>
    <div class="logo"><span class="mark"></span>PRESENTNEST</div>
    <div class="fsoc"><span></span><span></span><span></span><span></span></div>
    <div class="copy">© 2023 PRESENTNEST. All Rights Reserved.</div>
  </footer>

</div>
</body>
</html>
```